Business Card Design for Business Broker

Hi - I am looking for a cool design for my new business card using the logo attached.

We are business brokers. We help people buy and sell businesses!

I am open to just about anything. As far as colors, I do like the navy blue that is part of my logo.

Industry/Entity Type

Business

```html
<!DOCTYPE html>
<html lang="en">
<head>
<meta charset="utf-8">
<title>Harlow Reed – Business Card</title>
<link href="https://fonts.googleapis.com/css2?family=Roboto:wght@400;500;700&display=swap" rel="stylesheet">
<style>
  :root {
    --navy: #0b1a5c;
    --card-bg: #f0f1f1;
    --ink: #333333;
    --ink-soft: #555555;
    --tagline: #6b6b6b;
    --page: #ffffff;
  }
  html, body {
    margin: 0;
    padding: 0;
    width: 928px;
    height: 1200px;
    overflow: hidden;
    background: var(--page);
    font-family: "Roboto", Arial, sans-serif;
  }
  .sheet { position: relative; width: 928px; height: 1200px; }

  .card {
    position: absolute;
    left: 30px;
    width: 868px;
    height: 564px;
    box-sizing: border-box;
    border: 1.5px solid var(--navy);
    background: var(--card-bg);
    overflow: hidden;
  }
  .card--front { top: 26px; }
  .card--back  { top: 609px; }

  .block { position: absolute; background: var(--navy); width: 293px; }
  .card--front .block { left: 125px; }
  .card--back  .block { left: 288px; }
  .block--top    { top: 0; height: 233px; }
  .block--bottom { top: 332px; height: 232px; }

  .rule { position: absolute; top: 277px; height: 9px; background: var(--navy); }
  .rule--left   { left: 0; width: 93px; }
  .rule--middle { left: 455px; width: 284px; }
  .rule--right  { left: 775px; width: 93px; }

  .brand {
    position: absolute;
    top: 248px;
    width: 293px;
    text-align: center;
  }
  .card--front .brand { left: 125px; }
  .card--back  .brand { left: 288px; }
  .brand__name {
    display: block;
    font-weight: 400;
    font-size: 37px;
    line-height: 42px;
    letter-spacing: 1px;
    color: var(--navy);
    text-transform: uppercase;
  }
  .brand__tagline {
    display: block;
    margin-top: 2px;
    padding-bottom: 3px;
    border-bottom: 1px solid #c9c9c9;
    font-size: 17px;
    line-height: 22px;
    color: var(--tagline);
    letter-spacing: 0.2px;
  }

  .contact {
    position: absolute;
    right: 126px;
    text-align: right;
    color: var(--ink);
  }
  .person { top: 193px; }
  .person__name {
    margin: 0;
    font-weight: 700;
    font-size: 33px;
    line-height: 40px;
    color: var(--ink);
  }
  .person__surname { color: var(--navy); }
  .person__title {
    margin: 0;
    font-size: 20px;
    line-height: 26px;
    color: var(--ink-soft);
  }
  .details { top: 308px; font-size: 18px; line-height: 26px; }
  .details p { margin: 0; }
  .details .gap { margin-top: 22px; }
</style>
</head>
<body>
<div class="sheet">

  <section class="card card--front">
    <div class="block block--top"></div>
    <div class="block block--bottom"></div>
    <div class="rule rule--left"></div>
    <div class="rule rule--middle"></div>
    <div class="rule rule--right"></div>

    <div class="brand">
      <span class="brand__name">Harlow Reed</span>
      <span class="brand__tagline">Business Brokers &amp; Consultants</span>
    </div>

    <div class="contact person">
      <h1 class="person__name">JOHN <span class="person__surname">SMITH</span></h1>
      <p class="person__title">JOB TITLE</p>
    </div>

    <div class="contact details">
      <p>12345, MAIN STREET</p>
      <p>NM CITY</p>
      <p class="gap">+01 234 567 890</p>
      <p>email@yourdomain.com</p>
      <p>www.yourwebsite.com</p>
    </div>
  </section>

  <section class="card card--back">
    <div class="block block--top"></div>
    <div class="block block--bottom"></div>
    <div class="brand">
      <span class="brand__name">Harlow Reed</span>
      <span class="brand__tagline">Business Brokers &amp; Consultants</span>
    </div>
  </section>

</div>
</body>
</html>
```